Website home page template design for a not-for-profit organization.
Garden Valley Youth Coalition
Website home page template design for a not-for-profit organization. - Fund Raising
Creative Brief
Fund Raising
http://gardenvalley.unitedyouthcoalition.example/
Garden Valley Youth Coalition is a statewide non-profit membership organization whose mission is to promote and support communities in providing a coordinated investigation and comprehensive response to victims of criminal child abuse.
The logos for Garden Valley Youth Coalition and the United Youth Coalition must be present in the new design. All other aspects of the website, including the color palette can be changed.
below header
http://marloweshaven.example/
While the client likes the Marlowe's Haven website located at http://marloweshaven.example/, they are looking for an original design incorporating both their logo and the logo for United Youth Coalition. Please don't hesitate to contact me with any additional questions.

```html
<!DOCTYPE html>
<html lang="en">
<head>
<meta charset="utf-8">
<title>Garden Valley Youth Coalition</title>
<link href="https://fonts.googleapis.com/css2?family=PT+Sans:ital,wght@0,400;0,700;1,400;1,700&display=swap" rel="stylesheet">
<style>
:root{
  --bg:#ffffff;
  --page:#f3f3f3;
  --bar:#d9d9d9;
  --ink:#333333;
  --muted:#777777;
  --blue:#1f6fb2;
  --blue-dark:#155a93;
  --green:#6aa62a;
  --red:#d3232a;
  --purple:#6b3c97;
  --teal:#1aa3a3;
  --brown:#8a5a2b;
  --orange:#f0a21f;
}
*{box-sizing:border-box;margin:0;padding:0}
html,body{width:1200px;height:1052px;overflow:hidden;background:var(--bg);font-family:"PT Sans",Arial,sans-serif;color:var(--ink)}
.page{position:absolute;left:210px;top:34px;width:730px;height:974px;background:var(--page);box-shadow:0 0 18px rgba(0,0,0,.12)}
.topbar{position:absolute;left:0;top:0;width:100%;height:22px;background:var(--bar);font-size:10px}
.topbar .links{position:absolute;left:292px;top:5px;color:#444}
.topbar .search{position:absolute;left:530px;top:4px;width:70px;height:13px;background:#fff;border:1px solid #bbb}
.logo{position:absolute;left:105px;top:45px;width:130px;height:150px;background:#fff;border:1px solid #ddd;display:flex;flex-direction:column;align-items:center;justify-content:center;gap:8px;text-align:center}
.logo .mark{width:46px;height:46px;background:var(--blue)}
.logo .name{font-weight:700;font-size:13px;color:var(--blue-dark);line-height:1.2;padding:0 8px}
.newsletter{position:absolute;left:515px;top:48px;width:180px}
.newsletter h3{font-size:14px;font-weight:700;margin-bottom:4px}
.newsletter p{font-size:8px;color:var(--muted);margin-bottom:4px}
.newsletter .form{display:flex;gap:3px}
.newsletter .field{width:84px;height:11px;background:#fff;border:1px solid #bbb}
.newsletter .btn{width:34px;height:11px;background:#333}
.hero{position:absolute;left:91px;top:108px;width:550px;height:284px;background:linear-gradient(135deg,#e2503a,#f4b23b 35%,#3f9f4a 60%,#2f6fc0)}
.nav{position:absolute;left:91px;top:386px;width:550px;height:40px;display:flex;gap:2px}
.nav a{flex:1;color:#fff;font-size:8.5px;font-weight:700;padding:6px 5px;text-decoration:none;line-height:1.15;border-radius:3px 3px 0 0}
.features{position:absolute;left:91px;top:435px;width:550px;height:128px;display:flex;gap:4px}
.feature{flex:1;color:#fff;padding:8px 9px;position:relative;font-size:8px;line-height:1.35}
.feature h4{font-size:10.5px;font-weight:700;margin-bottom:5px;line-height:1.2}
.feature .more{position:absolute;right:8px;bottom:6px;font-size:7px}
.f-blue{background:linear-gradient(#2c86cf,var(--blue-dark))}
.f-green{background:linear-gradient(#86c23c,#5a9420)}
.cols{position:absolute;left:101px;top:586px;width:530px;display:flex;gap:30px}
.col{flex:1;position:relative;height:240px}
.col h2{font-size:15px;font-weight:700;font-style:italic;line-height:1.15;margin-bottom:8px}
.col h2.big{font-size:21px}
.col p{font-size:9px;font-style:italic;line-height:1.4;color:#444;margin-bottom:6px}
.col p b{font-weight:700}
.blue{color:var(--blue)}
.green{color:var(--green)}
.button{display:block;width:66px;height:16px;margin:10px auto 0;border-radius:3px;color:#fff;font-size:8px;font-weight:700;text-align:center;line-height:16px}
.b-blue{background:var(--blue)}
.b-green{background:var(--green)}
.footer{position:absolute;left:91px;top:860px;width:550px;height:80px;display:flex;justify-content:space-between;align-items:center}
.follow{font-size:9px;font-weight:700;text-align:center}
.icons{display:flex;gap:4px;margin-top:6px}
.icons span{width:14px;height:14px;border-radius:50%;display:block}
.partner{display:flex;align-items:center;gap:6px;font-size:10px;font-weight:700;color:var(--blue-dark)}
.partner .dot{width:22px;height:22px;border-radius:50%;background:var(--orange)}
.related{font-size:7px;color:#555;line-height:1.4}
.related b{font-size:8px;color:#333;display:block}
.copyright{position:absolute;left:0;top:950px;width:100%;text-align:center;font-size:7.5px;color:var(--muted)}
</style>
</head>
<body>
<div class="page">
  <div class="topbar">
    <span class="links">Contact Us &nbsp;|&nbsp; Login &nbsp;|&nbsp; Register</span>
    <span class="search"></span>
  </div>

  <div class="logo">
    <span class="mark"></span>
    <span class="name">Garden Valley Youth Coalition</span>
  </div>

  <div class="newsletter">
    <h3>Newsletter</h3>
    <p>Sign up for our Newsletter</p>
    <div class="form"><span class="field"></span><span class="btn"></span></div>
  </div>

  <div class="hero" role="img" aria-label="Photo of smiling children in bright shirts lying in a circle"></div>

  <nav class="nav">
    <a style="background:var(--red)">Garden Valley Home Page</a>
    <a style="background:var(--blue)">Youth Advocacy Centers</a>
    <a style="background:var(--purple)">Membership</a>
    <a style="background:var(--green)">Training and Events Calendar</a>
    <a style="background:var(--teal)">Child Welfare News</a>
    <a style="background:var(--brown)">State and County</a>
    <a style="background:var(--red)">UYC News</a>
    <a style="background:var(--orange)">Resources</a>
  </nav>

  <div class="features">
    <div class="feature f-blue">
      <h4>Welcome to the Garden Valley News and Event Site</h4>
      <p>Garden Valley Youth Coalition is a statewide membership group serving local communities.</p>
      <span class="more">View More &rsaquo;</span>
    </div>
    <div class="feature f-green">
      <h4>Mission and Vision</h4>
      <p>Lorem ipsum dolor sit amet, consectetur adipiscing elit. Cras tempor tincidunt quam, ac sollicitudin ipsum vehicula sit amet.</p>
      <span class="more">View More &rsaquo;</span>
    </div>
    <div class="feature f-blue">
      <h4>GVYC Member Contact Information</h4>
      <p>Northern region office hours and member listings for county teams across the valley.</p>
      <span class="more">View More &rsaquo;</span>
    </div>
    <div class="feature f-green">
      <h4>Garden Valley Multi-Disciplinary Teams (MDT's)</h4>
      <p>Lorem ipsum dolor sit amet, consectetur adipiscing elit, sed do eiusmod tempor.</p>
      <span class="more">View More &rsaquo;</span>
    </div>
  </div>

  <div class="cols">
    <div class="col">
      <h2 class="blue">The Purpose of Garden Valley Youth Coalition</h2>
      <p><b>Lorem ipsum dolor sit amet, consectetur adipiscing elit.</b> Cras tempor tincidunt quam ac sollicitudin. Etiam vehicula ipsum sit amet tempor, porttitor urna, quis tristique nibh.</p>
      <span class="button b-blue">Read More</span>
    </div>
    <div class="col">
      <h2 class="green big">In the news</h2>
      <p><b>Lorem ipsum dolor sit amet, consectetur adipiscing elit.</b> Cras tempor tincidunt quam, ac sollicitudin ipsum vehicula sit amet. Etiam tempor nibh.</p>
      <p>Nullam id nisl nulla. Sed in elementum mi. Sed quis neque nisl. Fusce venenatis augue a libero ornare.</p>
      <span class="button b-green">Read More</span>
    </div>
    <div class="col">
      <h2 class="blue big">Report abuse!</h2>
      <p><b>Lorem ipsum dolor sit amet, consectetur adipiscing elit.</b> Cras tempor tincidunt quam ac sollicitudin ipsum vehicula. Aliquam erat volutpat.</p>
      <p>Nullam id nisl nulla. Sed in elementum mi. Sed quis neque nisl. Fusce venenatis augue a libero ornare.</p>
      <span class="button b-blue">Report</span>
    </div>
  </div>

  <div class="footer">
    <div class="follow">Follow us:
      <div class="icons">
        <span style="background:var(--orange)"></span>
        <span style="background:var(--blue)"></span>
        <span style="background:var(--purple)"></span>
        <span style="background:var(--red)"></span>
      </div>
    </div>
    <div class="partner"><span class="dot"></span>United Youth Coalition</div>
    <div class="related"><b>Related Links</b>United Youth Coalition<br>Marlowe's Haven<br>Halvorsen Trust</div>
  </div>

  <div class="copyright">Garden Valley &nbsp;|&nbsp; &copy; 2012 All Rights Reserved &nbsp;|&nbsp; Privacy Policy</div>
</div>
</body>
</html>
```